Zielgruppe
Wir sind eine Lebküchnerei und möchten einen Flyer in 6-seitigen Wickelfalz Format. Unsere Zielgruppe sind mittelständische Unternehmen in ganz Deutschland.
Der Flyer soll einen ersten Eindruck auf unsere Produktvielfalt und die hohe Qualität der Lebkuchen vermitteln.
Aufgabenstellung
Passend zu unserer Website (Hintergrundfarbe RGB: Farbt: 30 Rot 255, Sätt. 240 Grün 208, Hell 151 Blau 66 HEX: FFD047) und Logo sollen Farbelemente in Gold und dunklem Rot zu finden sein. Daten bitte aus den angehängten Materialbild bzw. unserer Website (www.gebaeck-hornberg.de - wird gerade neu überarbeitet) entnehmen.
Unsere Produkte sind: Lebkuchen Konfekt, Lebkuchen als 3er oder 5er verpackt (sortenrein und sortiert), Walnuss-, Rum-Traube-Nuss- & Pistazienlebkuchen (jeweils 3er verpackt, nur sortenrein) sowie einzeln verpackte Lebkuchen und Geschenkdosen (verschiedene).
z. B. Vorderseite: unser Logo mit Webadresse, evtl. Lebkuchenbild Image; Rückseite: Kontakt und Standortinformationen
Wir bevorzugen mehrere Fotos, angehängte Fotos sollen als Beispiel dienen, Neuere sind in Bearbeitung und sollen später eingefügt/ersetzt werden.

```html
<!DOCTYPE html>
<html lang="de">
<head>
<meta charset="utf-8">
<title>Lebküchnerei Hornberg – Wickelfalz-Flyer</title>
<link rel="stylesheet" href="https://fonts.googleapis.com/css2?family=EB+Garamond:wght@400;500&family=Great+Vibes&display=swap">
<style>
  :root {
    --bg: #f4ecde;
    --red: #9a1a15;
    --red-deep: #8e1611;
    --gold: #c89b00;
    --gold-light: #e7b93a;
    --cream: #f7efe4;
    --ink: #3a2a22;
    --white: #ffffff;
  }
  * { margin: 0; padding: 0; box-sizing: border-box; }
  html, body { width: 1200px; height: 1200px; overflow: hidden; background: var(--bg); }
  body { position: relative; font-family: "EB Garamond", Georgia, serif; color: var(--ink); }

  .spread {
    position: absolute; left: 171px; width: 1190px; height: 800px;
    transform: scale(.72); transform-origin: 0 0;
    background: var(--cream); overflow: hidden;
    box-shadow: 0 4px 14px rgba(0,0,0,.18);
  }
  .spread--outside { top: 16px; }
  .spread--inside { top: 608px; }

  .header { position: absolute; left: 0; top: 0; width: 100%; height: 53px; background: var(--red); }
  .header__rule { position: absolute; left: 0; top: 53px; width: 100%; height: 7px; background: var(--white); }
  .header__title { position: absolute; top: 12px; color: var(--white); font-size: 24px; font-weight: 400; letter-spacing: .3px; }

  .footer { position: absolute; left: 0; top: 730px; width: 100%; height: 70px; background: var(--gold); border-top: 10px solid var(--red); }
  .footer__url { position: absolute; right: 44px; top: 6px; color: var(--white); font-size: 31px; letter-spacing: .5px; }

  .panel { position: absolute; top: 60px; height: 670px; }
  .panel--products { width: 392px; background: linear-gradient(180deg, #f3e9dc 0%, #eadccc 45%, #f0e5d8 100%); }
  .panel--red { background: var(--red-deep); }
  .panel--photo { background: radial-gradient(ellipse at 55% 60%, #9a5a2a 0%, #7a3e1e 30%, #c9884a 55%, #e3b884 75%, #f2e2cc 100%); }

  .product { position: absolute; left: 0; width: 392px; height: 200px; }
  .product__bar { position: absolute; left: 0; top: 0; width: 270px; height: 40px; background: var(--gold); }
  .product__bar--red { background: var(--red); }
  .product__name { position: absolute; left: 20px; top: 3px; z-index: 2; color: var(--white); font-family: "Great Vibes", cursive; font-size: 26px; white-space: nowrap; }
  .product__line { position: absolute; left: 19px; top: 52px; font-size: 13px; color: var(--ink); }
  .product__bullet { position: absolute; left: 19px; top: 73px; font-size: 13px; color: var(--ink); padding-left: 17px; }
  .product__bullet::before { content: ""; position: absolute; left: 0; top: 5px; width: 9px; height: 9px; border-radius: 50%; background: var(--ink); }
  .product__price { position: absolute; left: 19px; top: 102px; font-size: 12px; color: var(--ink); white-space: nowrap; }
  .product__price b { font-family: "Great Vibes", cursive; font-weight: 400; font-size: 30px; margin-left: 2px; }
  .product__image { position: absolute; left: 240px; top: -22px; width: 140px; height: 170px; z-index: 1; border-radius: 50% 50% 46% 46%; }
  .product__image--cookies { background: radial-gradient(circle at 40% 40%, #8a5a32 0%, #5a3219 55%, #3a1f10 100%); }
  .product__image--tins { background: linear-gradient(160deg, #c8222a 0%, #9e1419 60%, #6a0d10 100%); border-radius: 14px; }
  .product__image--pralines { background: radial-gradient(circle at 50% 50%, #7a4a22 0%, #3f2210 70%, #2a160a 100%); }
  .product__image--bag { background: linear-gradient(180deg, #e9e2d6 0%, #a57650 40%, #4a2a16 100%); border-radius: 30% 30% 40% 40%; height: 210px; }

  .contact { position: absolute; left: 28px; color: var(--white); font-size: 12.5px; line-height: 17.5px; }
  .contact--mail { font-size: 14.5px; line-height: 20px; }
  .hours { position: absolute; left: 28px; top: 548px; color: var(--white); font-size: 15px; line-height: 21px; }
  .hours__row { display: flex; }
  .hours__day { width: 125px; }

  .brand { position: absolute; display: flex; align-items: center; gap: 10px; }
  .brand__dot { border-radius: 50%; background: var(--white); border: 3px solid var(--gold); }
  .brand__name { font-family: "EB Garamond", Georgia, serif; font-weight: 500; color: var(--gold); }
  .brand--large { left: 878px; top: 30px; }
  .brand--large .brand__dot { width: 118px; height: 118px; }
  .brand--large .brand__name { font-size: 34px; }
  .brand--small { left: 552px; top: 512px; }
  .brand--small .brand__dot { width: 94px; height: 94px; }
  .brand--small .brand__name { font-size: 26px; color: var(--white); }

  .story {
    position: absolute; left: 791px; top: 60px; width: 399px; height: 670px;
    background: var(--red-deep); color: var(--white);
    padding: 28px 0 0 31px; display: flex; flex-direction: column; overflow: hidden;
  }
  .story__lead { width: 340px; font-size: 17px; line-height: 22px; margin-bottom: 14px; }
  .story__lead em, .story__gold { font-style: normal; color: var(--gold-light); }
  .story__text { width: 348px; font-size: 9.6px; line-height: 13.6px; margin-bottom: 10px; }
  .story__band { flex: none; height: 38px; margin: 2px 0 12px; background: var(--gold); color: var(--white); font-family: "Great Vibes", cursive; font-size: 23px; line-height: 38px; padding-left: 20px; white-space: nowrap; }
  .story__list { width: 348px; list-style: none; font-size: 9.6px; line-height: 13px; margin-bottom: 8px; }
  .story__list li { position: relative; padding-left: 18px; margin-bottom: 5px; }
  .story__list li::before { content: ""; position: absolute; left: 0; top: 3px; width: 8px; height: 8px; border-radius: 50%; background: var(--white); }
  .story__closing { margin-top: auto; padding-bottom: 10px; }
  .story__closing .story__band { margin: 0 0 6px; }
  .story__sign { color: var(--gold-light); font-size: 12px; line-height: 17px; }
</style>
</head>
<body>

<section class="spread spread--outside">
  <div class="panel panel--products" style="left:0" role="img" aria-label="Blass eingeblendetes Lebkuchenfoto als Hintergrund"></div>
  <div class="panel panel--red" style="left:392px; width:399px;"></div>
  <div class="panel panel--photo" style="left:791px; width:399px;" role="img" aria-label="Foto: Elisenlebkuchen mit Mandeln, Schokolade, Nüssen und Zutaten in Glasschalen"></div>

  <div class="header"></div>
  <div class="header__rule"></div>
  <h2 class="header__title" style="left:20px">Geschenkverpackungen</h2>
  <h2 class="header__title" style="left:420px">Kontakt</h2>

  <div class="product" style="top:98px">
    <div class="product__bar"></div>
    <div class="product__name">Elisenlebkuchen, 3er</div>
    <p class="product__line">Original Elisenlebkuchen, sortiert</p>
    <p class="product__bullet">wählen Sie Ihre Sorten aus</p>
    <p class="product__price">240 g ab <b>5,70 €</b></p>
    <div class="product__image product__image--cookies" role="img" aria-label="Foto: drei Elisenlebkuchen, schokoliert und mit Mandeln"></div>
  </div>
  <div class="product" style="top:331px">
    <div class="product__bar"></div>
    <div class="product__name">Geschenkdosen, 2er Set</div>
    <p class="product__line">Schicke Geschenkdosen</p>
    <p class="product__bullet">wählen Sie Ihre Lieblingsdose</p>
    <p class="product__price">Set nur <b>5,70 €</b></p>
    <div class="product__image product__image--tins" role="img" aria-label="Foto: zwei rote Geschenkdosen mit Wintermotiv"></div>
  </div>
  <div class="product" style="top:558px">
    <div class="product__bar"></div>
    <div class="product__name">Geschenktüte gefüllt</div>
    <p class="product__line">Original Elisenlebkuchen, sortiert</p>
    <p class="product__bullet">wählen Sie Ihre Sorten aus</p>
    <p class="product__price">240 g ab <b>5,70 €</b></p>
    <div class="product__image product__image--bag" role="img" aria-label="Foto: gefüllte Geschenktüte mit Elisenlebkuchen"></div>
  </div>

  <p class="contact" style="left:420px; top:103px">Hauptsitz Fürth<br>Lindenstraße 12<br>90762 Fürth<br>Tel: 0911 550123</p>
  <p class="contact" style="left:420px; top:190px">Zabo Nürnberg<br>Gartenstraße 8<br>Ecke Brunnenweg<br>90482 Nürnberg<br>Tel: 0911 3390458</p>
  <p class="contact contact--mail" style="left:420px; top:297px">e-mail: info@gebaeck-hornberg.de<br>www.gebaeck-hornberg.de</p>

  <div class="brand brand--small"><span class="brand__dot"></span><span class="brand__name">Hornberg</span></div>

  <div class="hours" style="left:420px; top:605px">
    <p>Öffnungszeiten</p>
    <p class="hours__row"><span class="hours__day">Montag - Freitag:</span><span>6.00 - 18.00 Uhr</span></p>
    <p class="hours__row"><span class="hours__day">Samstag:</span><span>6.00 - 12.30 Uhr</span></p>
    <p class="hours__row"><span class="hours__day">Sonntag:</span><span>8.00 - 11.00 Uhr</span></p>
  </div>

  <div class="brand brand--large"><span class="brand__dot"></span><span class="brand__name">Hornberg</span></div>

  <div class="footer"><span class="footer__url">www.gebaeck-hornberg.de</span></div>
</section>

<section class="spread spread--inside">
  <div class="panel panel--products" style="left:0; width:791px;" role="img" aria-label="Blass eingeblendetes Foto von Lebkuchen und Gewürzen als Hintergrund"></div>

  <div class="header"></div>
  <div class="header__rule"></div>
  <h2 class="header__title" style="left:27px">Feine Auswahl</h2>
  <h2 class="header__title" style="left:420px">Feine Auswahl</h2>
  <h2 class="header__title" style="left:820px">Familienbetrieb mit Tradition</h2>

  <div class="product" style="top:97px">
    <div class="product__bar product__bar--red"></div>
    <div class="product__name">Elisenlebkuchen, 3er</div>
    <p class="product__line">Original Elisenlebkuchen, sortiert</p>
    <p class="product__bullet">wählen Sie Ihre Sorten aus</p>
    <p class="product__price">240 g ab <b>5,70 €</b></p>
    <div class="product__image product__image--cookies" role="img" aria-label="Foto: drei Elisenlebkuchen"></div>
  </div>
  <div class="product" style="top:331px">
    <div class="product__bar product__bar--red"></div>
    <div class="product__name">Geschenkdosen, 2er Set</div>
    <p class="product__line">Schicke Geschenkdosen</p>
    <p class="product__bullet">wählen Sie Ihre Lieblingsdose</p>
    <p class="product__price">Set nur <b>5,70 €</b></p>
    <div class="product__image product__image--pralines" role="img" aria-label="Foto: Lebkuchen-Konfekt mit Nüssen"></div>
  </div>
  <div class="product" style="top:558px">
    <div class="product__bar product__bar--red"></div>
    <div class="product__name">Geschenktüte gefüllt</div>
    <p class="product__line">Original Elisenlebkuchen, sortiert</p>
    <p class="product__bullet">wählen Sie Ihre Sorten aus</p>
    <p class="product__price">240 g ab <b>5,70 €</b></p>
    <div class="product__image product__image--bag" role="img" aria-label="Foto: gefüllte Geschenktüte mit Elisenlebkuchen"></div>
  </div>

  <div class="product" style="left:420px; top:97px">
    <div class="product__bar"></div>
    <div class="product__name">Elisenlebkuchen, 3er</div>
    <p class="product__line">Original Elisenlebkuchen, sortiert</p>
    <p class="product__bullet">wählen Sie Ihre Sorten aus</p>
    <p class="product__price">240 g ab <b>5,70 €</b></p>
    <div class="product__image product__image--cookies" role="img" aria-label="Foto: drei Elisenlebkuchen"></div>
  </div>
  <div class="product" style="left:420px; top:331px">
    <div class="product__bar"></div>
    <div class="product__name">Geschenkdosen, 2er Set</div>
    <p class="product__line">Schicke Geschenkdosen</p>
    <p class="product__bullet">wählen Sie Ihre Lieblingsdose</p>
    <p class="product__price">Set nur <b>5,70 €</b></p>
    <div class="product__image product__image--pralines" role="img" aria-label="Foto: Lebkuchen-Konfekt mit Nüssen"></div>
  </div>
  <div class="product" style="left:420px; top:558px">
    <div class="product__bar"></div>
    <div class="product__name">Geschenktüte gefüllt</div>
    <p class="product__line">Original Elisenlebkuchen, sortiert</p>
    <p class="product__bullet">wählen Sie Ihre Sorten aus</p>
    <p class="product__price">240 g ab <b>5,70 €</b></p>
    <div class="product__image product__image--bag" role="img" aria-label="Foto: gefüllte Geschenktüte mit Elisenlebkuchen"></div>
  </div>

  <article class="story">
    <p class="story__lead">Wir sind ein Familienbetrieb mit 60-jähriger Backtradition und eine der <em>DREI !!! letzten noch bestehenden Handwerksbäckereien in Fürth.</em></p>
    <p class="story__text">Ausgehend vom väterlichen Stammbetrieb in der Mühlstraße am idyllischen Dutzendteich in Nürnberg besteht heute der Betrieb mit durchschnittlich 35 Mitarbeitern in der Lindenstraße im Süden Fürths.</p>
    <p class="story__text"><span class="story__gold">In einer Bäckerfamilie geboren</span> und von klein auf bei Papa in der Backstube, war klar das es nur eines gibt, ich wollte und wurde Bäcker!</p>
    <div class="story__band">Bäcker = eine noch immer ehrenvolle Aufgabe</div>
    <ul class="story__list">
      <li>Ich legte im Jahr 1985 meine Gesellenprüfung im Bäckerhandwerk erfolgreich ab, 1991 folgte die Meisterprüfung.</li>
      <li>Es folgten verschiedene Aufenthalte im europäischen Ausland, u.a. bei der Confiserie Albrecht in St. Moritz (Schweiz)</li>
      <li>Die Kunst des Pralinenherstellens - das Highlight meiner bisherigen Ausbildung!</li>
    </ul>
    <p class="story__text"><span class="story__gold">Am 1. März 1994 übernahm ich die Bäckerei meiner Eltern,</span> Anna und Ernst Hornberg, die sie gemeinsam seit dem 1. Mai 1959 führten. 1997 heiratete ich Nicole Hornberg, geb. Keller und am 1. Oktober 2003 wurde mit der Übernahme der traditionsreichen und weit über die Grenzen Fürths hinaus bekannten Bäckerei Sommer ein richtungsweisender Weg für die Zukunft eingeschlagen.</p>
    <p class="story__text">In unseren Läden erfüllen unsere kompetenten und stets freundlichen und zuvorkommenden Verkäuferinnen die Wünsche der Kunden. Dazu trägt auch der Schwerpunkt meines bisherigen Betriebes in Nürnberg bei. Dort war mein Hauptaugenmerk auf die Belieferung von Hotels der gehobenen Klasse sowie namhaften Kantinen und Wiederverkäufern gerichtet.</p>
    <div class="story__closing">
      <div class="story__band">Sie als Kunde zufriedenzustellen</div>
      <p class="story__sign">Ihr Bäckermeister<br>Markus Hornberg</p>
    </div>
  </article>

  <div class="footer"></div>
</section>

</body>
</html>
```